Commercial and Multifamily informational website

We need a website for our commercial real estate management company. We will manage offices, retail, apartments and others. Here is the brief verbiage: Providing quality commercial and multifamily portfolio management to Landlords, REITs, and financial institutions. 

Industry/Entity Type

Real Estate

Number of Pages Required

2 page

Font styles to use
Sans Serif
Other font styles liked:
• Muli, Garamond

Colors
0555a3
5c5c5c
3176b5
85acd3
474747

Requirements
Must have
• Home page and contact page

```html
<!DOCTYPE html>
<html lang="en">
<head>
<meta charset="utf-8">
<title>Northvale Property Management</title>
<link rel="stylesheet" href="https://fonts.googleapis.com/css2?family=Mulish:wght@400;600;700&family=Open+Sans:wght@400;600&display=swap">
<style>
:root{
  --blue:#0555a3;
  --blue-mid:#3176b5;
  --blue-light:#85acd3;
  --text:#474747;
  --text-soft:#5c5c5c;
  --muted:#8a8a8a;
  --gray-band:#f2f2f2;
  --white:#ffffff;
}
*{box-sizing:border-box;margin:0;padding:0}
html,body{width:1200px;height:2691px;overflow:hidden;background:var(--white)}
body{font-family:"Open Sans",Arial,sans-serif;color:var(--text);position:relative}
.abs{position:absolute}
.heading{font-family:"Mulish",Arial,sans-serif}

/* header */
.site-header{position:absolute;left:0;top:0;width:1200px;height:115px;background:var(--white)}
.brand{position:absolute;left:129px;top:36px;display:flex;align-items:center;gap:12px}
.brand-mark{width:40px;height:40px;background:var(--blue)}
.brand-name{font-family:"Mulish",Arial,sans-serif;font-weight:700;font-size:19px;line-height:20px;color:var(--blue);text-transform:uppercase;width:220px}
.main-nav a{position:absolute;top:49px;font-family:"Mulish",Arial,sans-serif;font-size:16px;font-weight:600;color:#333;text-decoration:none;letter-spacing:.3px}
.main-nav a.active{color:var(--blue)}
.nav-underline{position:absolute;left:502px;top:109px;width:59px;height:5px;background:var(--blue)}

/* hero */
.hero{position:absolute;left:0;top:115px;width:1200px;height:572px;background:linear-gradient(120deg,#e9eaec 0%,#c9c8c6 40%,#a7a29c 62%,#d8d9db 100%)}
.hero-text{position:absolute;left:0;top:235px;width:1200px;text-align:center;color:var(--white);font-family:"Mulish",Arial,sans-serif;font-weight:700;font-size:32px;line-height:42px;text-shadow:0 1px 4px rgba(0,0,0,.25)}
.hero-dots{position:absolute;left:550px;top:643px;display:flex;gap:8px}
.hero-dots span{width:15px;height:15px;border-radius:50%;background:var(--white)}
.hero-dots span.current{background:transparent;border:2px solid var(--white)}

/* company */
.company{position:absolute;left:0;top:687px;width:1200px;height:479px;background:var(--blue);color:var(--white);text-align:center}
.company h2{margin-top:80px;font-family:"Mulish",Arial,sans-serif;font-weight:400;font-size:27px;letter-spacing:.5px}
.company p{width:860px;margin:26px auto 0;font-size:15px;line-height:29px;color:#dbe6f3}
.btn-outline{display:inline-block;font-family:"Mulish",Arial,sans-serif;font-weight:600;text-transform:uppercase;text-decoration:none}
.company .btn-outline{margin-top:30px;width:158px;height:43px;line-height:39px;border:2px solid var(--white);color:var(--white);font-size:17px}

/* services */
.service{position:absolute;top:1039px;width:307px;text-align:center}
.service-frame{background:var(--white);padding:9px 10px 0;height:193px}
.service-photo{height:184px}
.service h3{margin-top:30px;font-family:"Mulish",Arial,sans-serif;font-weight:600;font-size:23px;color:#333}
.service p{width:280px;margin:6px auto 0;font-size:13px;line-height:18px;color:var(--muted)}
.service .btn-outline{margin-top:18px;width:111px;height:30px;line-height:27px;border:1.5px solid var(--blue);color:var(--blue);font-size:12px}

/* news */
.news{position:absolute;left:0;top:1471px;width:1200px;height:409px;background:var(--gray-band)}
.news h2{position:absolute;left:149px;top:74px;font-family:"Mulish",Arial,sans-serif;font-weight:400;font-size:28px;color:#222}
.news-item{position:absolute;top:128px;width:420px}
.news-date{font-family:"Mulish",Arial,sans-serif;font-size:17px;color:var(--blue-mid)}
.news-title{margin-top:8px;font-family:"Mulish",Arial,sans-serif;font-weight:600;font-size:19px;line-height:24px;color:var(--blue-mid)}
.news-body{margin-top:20px;font-size:13.5px;line-height:23px;color:var(--text-soft)}

/* projects */
.projects-title{position:absolute;left:0;top:1920px;width:1200px;text-align:center;font-family:"Mulish",Arial,sans-serif;font-weight:700;font-size:24px;color:var(--blue)}
.project{position:absolute;top:1982px;width:218px;height:228px}
.project-overlay{position:absolute;inset:0;background:rgba(5,85,163,.55);color:var(--white);text-align:center;padding-top:90px}
.project-overlay strong{display:block;font-family:"Mulish",Arial,sans-serif;font-size:16px}
.project-overlay small{display:block;width:150px;margin:4px auto 0;font-size:11px;line-height:15px}

/* footer */
.site-footer{position:absolute;left:0;top:2298px;width:1200px;height:393px;background:linear-gradient(180deg,#7b7b7b 0%,#4b4b4b 45%,#2f2f2f 100%);color:var(--white)}
.footer-col{position:absolute;top:62px}
.footer-col h4{font-family:"Mulish",Arial,sans-serif;font-weight:400;font-size:19px;letter-spacing:.3px;margin-bottom:8px}
.footer-col li{list-style:none;font-size:14px;line-height:27px;color:#eee}
.social{display:flex;gap:3px;margin-top:6px}
.social span{width:38px;height:38px;border-radius:50%;background:#9a9a9a}
.footer-rule{position:absolute;left:135px;top:305px;width:938px;height:1px;background:#777}
.copyright{position:absolute;left:0;top:332px;width:1200px;text-align:center;font-size:12px;color:#ccc}
</style>
</head>
<body>

<header class="site-header">
  <div class="brand"><span class="brand-mark"></span><span class="brand-name">Northvale Property<br>Management</span></div>
  <nav class="main-nav">
    <a class="active" style="left:504px">HOME</a>
    <a style="left:594px">ABOUT</a>
    <a style="left:691px">SERVICES</a>
    <a style="left:804px">TEAM</a>
    <a style="left:890px">NEWS</a>
    <a style="left:978px">CONTACT</a>
  </nav>
  <div class="nav-underline"></div>
</header>

<section class="hero" role="img" aria-label="Overhead photo of a handshake over a desk with keys, a tablet and a small house model"></section>
<h1 class="hero-text">Providing quality commercial and<br>multifamily portfolio management to Landlords,<br>REITs, and financial institutions.</h1>
<div class="hero-dots"><span class="current"></span><span></span><span></span><span></span></div>

<section class="company">
  <h2>OUR COMPANY</h2>
  <p>Praesent elementum elit at tellus nec ultricies sit amet porttitor mattis enim In massa libero interdum nec interdum vel blandit sed nulla In ullamcorper est eget tempor cursus neque mi consectetuer mi a ultricies massa est sed nisl Class aptent taciti sociosqu ad litora torquent per conubia nostra per</p>
  <a class="btn-outline">Read More</a>
</section>

<article class="service" style="left:135px">
  <div class="service-frame"><div class="service-photo" role="img" aria-label="Glass office towers against a blue sky" style="background:linear-gradient(160deg,#9cc3e6,#3d6f9e 60%,#2a4a6b)"></div></div>
  <h3>OFFICES</h3>
  <p>Morbi diam mauris viverra in gravida eu mattis in ante Morbi eget arcu Morbi porta libero id ullamcorper nonummy</p>
  <a class="btn-outline">Read More</a>
</article>
<article class="service" style="left:451px">
  <div class="service-frame"><div class="service-photo" role="img" aria-label="Modern apartment building with balconies at sunset" style="background:linear-gradient(160deg,#bcd3e2,#d9c9a8 50%,#6b6660)"></div></div>
  <h3>APARTMENTS</h3>
  <p>Morbi diam mauris viverra in gravida eu mattis in ante Morbi eget arcu Morbi porta libero id ullamcorper nonummy</p>
  <a class="btn-outline">Read More</a>
</article>
<article class="service" style="left:767px">
  <div class="service-frame"><div class="service-photo" role="img" aria-label="Multi-storey residential homes with balconies" style="background:linear-gradient(160deg,#7fb0e0,#cfc6b8 55%,#8f8a80)"></div></div>
  <h3>HOMES</h3>
  <p>Morbi diam mauris viverra in gravida eu mattis in ante Morbi eget arcu Morbi porta libero id ullamcorper nonummy</p>
  <a class="btn-outline">Read More</a>
</article>

<section class="news">
  <h2>LATEST NEWS</h2>
  <div class="news-item" style="left:152px">
    <div class="news-date">25 Feb 2016</div>
    <div class="news-title">Mauris vel lacus vitae felis vestibulum volutpat Etiam est nunc venenatis</div>
    <p class="news-body">nisl Cum sociis natoque penatibus et magnis dis parturient montes nascetur ridiculus mus In iaculis facilisis massMorbi diam mauris viverra in gravida eu mattis in</p>
  </div>
  <div class="news-item" style="left:655px">
    <div class="news-date">15 Feb 2016</div>
    <div class="news-title">Duis quam Nam eget lacus Aliquam erat volutpat Quisque</div>
    <p class="news-body">nisl Cum sociis natoque penatibus et magnis dis parturient montes nascetur ridiculus mus In iaculis facilisis massMorbi diam mauris viverra in gravida eu mattis in</p>
  </div>
</section>

<h2 class="projects-title">LATEST PROJECTS</h2>
<div class="project" style="left:135px" role="img" aria-label="White apartment block with greenery under a blue sky" style="background:#ccc"></div>
<div class="project" style="left:135px;background:linear-gradient(170deg,#a9cbe9,#d8d2c4 55%,#6f7a5a)" role="img" aria-label="White apartment block with greenery under a blue sky"></div>
<div class="project" style="left:375px;background:linear-gradient(170deg,#b8c7d6,#7f93a8 60%,#6c7c62)" role="img" aria-label="Apartment row along a quiet street">
  <div class="project-overlay"><strong>Class aptent taciti</strong><small>Proin nulla arcu non metus luctus dictum eget fermentum</small>
    <svg width="14" height="10" viewBox="0 0 14 10" style="margin-top:6px"><path d="M2 2l5 5 5-5" fill="none" stroke="#fff" stroke-width="2"/></svg></div>
</div>
<div class="project" style="left:615px;background:linear-gradient(175deg,#c9ced3,#8b8f94 55%,#3a4654)" role="img" aria-label="Waterfront apartment towers at dusk"></div>
<div class="project" style="left:856px;background:linear-gradient(135deg,#f6d58a,#c48a4f 45%,#6a4a35)" role="img" aria-label="Brick apartment facade lit by golden sunlight"></div>

<footer class="site-footer">
  <div class="footer-col" style="left:152px"><h4>COMPANY</h4><ul><li>Home</li><li>About Us</li><li>Our Services</li><li>Why Us</li></ul></div>
  <div class="footer-col" style="left:357px"><h4>RESOURCES</h4><ul><li>Support</li><li>Solutions</li><li>Testimonials</li><li>Contact Us</li></ul></div>
  <div class="footer-col" style="left:545px"><h4>FOLLOW US</h4><div class="social"><span></span><span></span><span></span><span></span></div></div>
  <div class="footer-col" style="left:802px"><h4>CONTACT INFO</h4><ul><li>417 Harbor Point Road Suite 210</li><li>Millbrook, PA 18900</li><li>(555) 014-2780</li><li>info@northvaleproperty.com</li></ul></div>
  <div class="footer-rule"></div>
  <p class="copyright">© 2017 Company Name &nbsp;All right reserved &nbsp;Term of Use</p>
</footer>

</body>
</html>
```